Bref créative
Business cards and stationary Hospitality group company in Mexico
subtitle is optional "Hospitalidad Hecho en Mexico"
I need double sided standard sized Business Card [3.5" x 2"]
I like the fonts used in my logo but we are open to new fonts or more than one if necessary
Modern
Gerardo Villena
4871 Almendros
Col. Santa Brígida
Monterrey, NL México
CP 67215
beto@qvral.mx
www.qvral.mx
I am looking for a modern design, I like those colors but feel free to play with the colors if you have an idea..
QV ALBERGANTE

```html
<!DOCTYPE html>
<html lang="es">
<head>
<meta charset="utf-8">
<title>QV Albergante – Tarjeta de presentación</title>
<link rel="stylesheet" href="https://fonts.googleapis.com/css2?family=Arimo:wght@400;700&display=swap">
<style>
  :root {
    --stage: #e9e7e2;
    --card-top: #3b3b3d;
    --card-bottom: #262627;
    --orange: #ee5a2a;
    --orange-light: #f4843f;
    --text-light: #d9d9d9;
    --text-muted: #9a9a9a;
    --rule: #6d6d6d;
    --band-grey: #8c8c8c;
    --white: #ffffff;
  }
  * { margin: 0; padding: 0; box-sizing: border-box; }
  html, body { width: 1200px; height: 871px; overflow: hidden; }
  body {
    background: var(--stage);
    font-family: "Arimo", Arial, sans-serif;
    display: flex;
    flex-direction: column;
    align-items: center;
    justify-content: center;
    gap: 23px;
  }
  .card {
    position: relative;
    width: 700px;
    height: 400px;
    border-radius: 14px;
    background: linear-gradient(160deg, var(--card-top), var(--card-bottom));
    overflow: hidden;
    box-shadow: 0 6px 18px rgba(0,0,0,.18);
  }

  /* Back side */
  .back-mark {
    position: absolute;
    left: 70px; top: 90px;
    width: 190px; height: 190px;
    border-radius: 50%;
    background: rgba(238,90,42,.12);
  }
  .back-name {
    position: absolute;
    left: 300px; top: 160px;
    font-size: 40px; font-weight: 700;
    letter-spacing: 1px;
    color: var(--text-light);
  }
  .back-web {
    position: absolute;
    left: 302px; top: 212px;
    font-size: 20px; font-weight: 700;
    letter-spacing: 4px;
    color: var(--orange);
  }

  /* Front side */
  .brand {
    position: absolute;
    left: 40px; top: 170px;
    display: flex; align-items: center; gap: 10px;
  }
  .brand-square { width: 22px; height: 22px; background: var(--orange); }
  .brand-name {
    font-size: 20px; font-weight: 700;
    color: var(--white);
    letter-spacing: .5px;
  }
  .divider {
    position: absolute;
    left: 272px; top: 40px;
    width: 1px; height: 255px;
    background: var(--rule);
  }
  .contact {
    position: absolute;
    left: 300px; top: 50px;
    color: var(--text-light);
  }
  .contact-name {
    font-size: 22px; font-weight: 700;
    color: var(--orange);
    margin-bottom: 18px;
  }
  .address { font-size: 16px; line-height: 21px; }
  .reach {
    display: flex; gap: 12px;
    margin-top: 26px;
  }
  .phone-icon { width: 18px; height: 34px; margin-top: 2px; }
  .reach-lines { font-size: 16px; line-height: 21px; }
  .band-rule {
    position: absolute;
    left: 0; right: 0; top: 318px; height: 4px;
    background: var(--band-grey);
  }
  .web-band {
    position: absolute;
    left: 0; right: 0; top: 326px; height: 46px;
    background: linear-gradient(90deg, var(--orange), var(--orange-light), var(--orange));
    display: flex; align-items: center; justify-content: center;
  }
  .web-address {
    font-size: 16px; font-weight: 700;
    letter-spacing: 5px;
    color: var(--white);
  }
</style>
</head>
<body>

  <section class="card card-back" aria-label="Reverso de la tarjeta">
    <div class="back-mark"></div>
    <div class="back-name">QV ALBERGANTE</div>
    <div class="back-web">qvral.mx</div>
  </section>

  <section class="card card-front" aria-label="Frente de la tarjeta">
    <div class="brand">
      <span class="brand-square"></span>
      <span class="brand-name">QV ALBERGANTE</span>
    </div>

    <div class="divider"></div>

    <div class="contact">
      <div class="contact-name">Gerardo Villena</div>
      <div class="address">
        4871 Almendros<br>
        Col. Santa Brígida<br>
        Monterrey, NL México<br>
        CP 67215
      </div>
      <div class="reach">
        <svg class="phone-icon" viewBox="0 0 18 34" aria-hidden="true">
          <rect x="2" y="1" width="14" height="32" rx="3" fill="none" stroke="#ee5a2a" stroke-width="2"/>
          <rect x="5" y="5" width="8" height="14" fill="#ee5a2a"/>
          <circle cx="9" cy="27" r="2" fill="#ee5a2a"/>
        </svg>
        <div class="reach-lines">
          (81) 4670 3185<br>
          (81) 4593 7206<br>
          beto@qvral.mx
        </div>
      </div>
    </div>

    <div class="band-rule"></div>
    <div class="web-band">
      <span class="web-address">www.qvral.mx</span>
    </div>
  </section>

</body>
</html>
```